Tidal Bloomz - Sovereign rings, pendants & custom cultural pieces

I need a website that attracts customers knowing that I am as per detailed below Everyone deserves a special piece of treasure. At Tidal Bloomz we provide you with unique, high-quality and affordable Sovereign rings, pendants & custom cultural pieces.
Feel free to check my Picorama page to get idea's @tidal.bloomz
I want people to see the Items I have available & know that my prices are very competitive. I want people to be able to Shop/Purchase items via site. I would like to have Tidal Bloomz Friendlio, Picorama & Swapzo Icon/tabs on site so customers can link a at click of the mouse.

(My Apologies to you all, This is all overwhelming & new to myself & I appreciate your efforts & work detail)
Updates

Apologies, have had family loss to deal with

Still dealing with loss of family member

Still Dealing with Family member passing

As previously, still getting through the loss of a family member

As per previous extensions, re adjusting to life after loss of family member

As per previously still recovering from loss of family member

As previously expressed

Haven’t recovered from family loss

I am still getting life back together

Target Market(s)

Jewellery, Wedding, Gifts, Pacific people, Persons 18 - 65yrs, New Zealand & Australian

Industry/Entity Type

Jewelry

Contact Information for Business Card

Tidal Bloomz
Reko Tumanu
Friendlio @tidalbloomz
Picorama @tidal.bloomz
Phone Number 021 07351942
Website www.tidalbloomz-example.co.nz
Auckland
New Zealand

Number of Pages Required

5+ page

Font styles to use
Sans Serif

Colors
474747
1b1b1b
000000
cfcfcf
fbed22
ffc214
ffffff

Requirements
Must have
• Using Black / Gold Tidal Bloomz logo with crown, has been attached to Web design.
• Reko Tumanu
• Friendlio Tidal Bloomz
• Picorama @tidal.bloomz
• Swapzo Tidal Bloomz
• Phone Number 021 07351942
• Website www.tidalbloomz-example.co.nz
Nice to have
• Thinking black card with the Tidal Bloomz Gold logo
• Lines on back of card for Customer Quoted Prices

```html
<!DOCTYPE html>
<html lang="en">
<head>
<meta charset="utf-8">
<title>Tidal Bloomz – Sovereign Rings, Pendants &amp; Custom Cultural Pieces</title>
<link href="https://fonts.googleapis.com/css2?family=Montserrat:wght@400;500;600;700&family=Open+Sans:wght@400;600&display=swap" rel="stylesheet">
<style>
:root{
  --black:#000000;
  --ink:#1b1b1b;
  --grey:#474747;
  --silver:#cfcfcf;
  --light:#f1f1f1;
  --gold:#ffc214;
  --lemon:#fbed22;
  --white:#ffffff;
  --red:#e3262b;
  --muted:#8a8a8a;
}
*{box-sizing:border-box;margin:0;padding:0}
html,body{width:1200px;height:4000px;overflow:hidden;background:var(--white)}
body{position:relative;font-family:"Open Sans",sans-serif;color:var(--ink)}
.abs{position:absolute}
h1,h2,h3,h4,.btn,.menu a,.tabs span{font-family:"Montserrat",sans-serif}

/* header */
.topbar{left:0;top:0;width:1200px;height:73px;background:var(--black)}
.burger{left:40px;top:27px;width:24px}
.burger i{display:block;height:3px;background:var(--white);margin-bottom:5px}
.brand{left:540px;top:0;width:120px;height:92px;background:var(--black);display:flex;flex-direction:column;align-items:center;justify-content:center;gap:6px;z-index:3}
.brand-dot{width:16px;height:16px;background:var(--gold);border-radius:50%}
.brand-name{font-family:"Montserrat",sans-serif;font-weight:600;font-size:14px;color:var(--gold);letter-spacing:.5px}
.head-tools{right:40px;top:26px;display:flex;align-items:center;gap:18px;color:var(--white);font-size:14px;font-family:"Montserrat",sans-serif}
.head-tools .phone{display:flex;align-items:center;gap:8px}

/* hero */
.hero{left:0;top:73px;width:1200px;height:577px;background:linear-gradient(100deg,#2d2a25 0%,#6b5a3c 22%,#a8853f 34%,#5e554a 50%,#7e7c79 70%,#a6a5a3 100%)}
.hero-title{left:650px;top:140px;font-family:"Montserrat",sans-serif;font-weight:500;font-size:42px;line-height:56px;letter-spacing:2px;color:var(--white)}
.hero-title em{font-style:normal;color:var(--gold)}
.hero-arrow{top:290px;width:38px;height:38px;background:var(--white);display:flex;align-items:center;justify-content:center}
.thumbs{left:207px;top:467px;display:flex;gap:32px}
.thumb{width:136px;height:166px;border:3px solid var(--white);background:linear-gradient(135deg,#8b8680,#cbb38a 50%,#6d6a66)}
.thumb-arrow{top:537px;width:22px;height:26px;background:var(--gold);display:flex;align-items:center;justify-content:center}

/* side menu & sale */
.menu{left:170px;top:730px;width:190px}
.menu a{display:block;font-size:12px;font-weight:600;color:var(--ink);text-decoration:none;padding:10px 0;border-bottom:1px solid #e2e2e2;letter-spacing:.3px}
.menu a .new{color:var(--red)}
.sale{left:393px;top:727px;width:634px;height:300px;background:linear-gradient(90deg,#dadada,#bdbdbd 55%,#9e9e9e)}
.sale-copy{left:60px;top:60px}
.sale-copy h2{font-size:58px;font-weight:700;color:var(--ink);line-height:62px}
.sale-copy p{font-family:"Montserrat",sans-serif;font-weight:600;font-size:20px;color:var(--ink);margin-top:4px}
.sale-copy .sub{font-size:14px;margin-top:10px}
.sale-photo{right:40px;top:30px;width:240px;height:240px;border-radius:50%;background:radial-gradient(circle,#e9e6e0,#bfb9ad 55%,#8e8a84)}
.btn-gold{display:inline-block;background:var(--gold);color:var(--ink);font-size:12px;font-weight:600;padding:12px 28px;letter-spacing:.5px;white-space:nowrap}

/* products */
.section-title{left:0;width:1200px;text-align:center;font-size:28px;font-weight:600;letter-spacing:1px;color:var(--ink)}
.tabs{left:0;top:1170px;width:1200px;display:flex;justify-content:center;gap:26px}
.tabs span{font-size:13px;font-weight:500;color:var(--grey);padding-bottom:6px}
.tabs span.on{color:var(--ink);border-bottom:2px solid var(--gold)}
.product{width:194px;text-align:center}
.product .shot{width:194px;height:257px;background:linear-gradient(140deg,#7b7876,#bdb3a1 50%,#5f5c59)}
.product h4{font-size:10px;font-weight:600;margin-top:22px;color:var(--ink);white-space:nowrap}
.price{display:inline-block;margin-top:10px;border:1px solid var(--silver);padding:4px 18px;font-size:12px;color:var(--gold);font-family:"Montserrat",sans-serif;font-weight:600}
.price s{color:var(--muted);margin-right:8px}
.view-more{left:533px;top:2003px;width:134px;text-align:center;padding:12px 0}

/* feature blocks */
.photo{background:linear-gradient(135deg,#3a3a3a,#7a6a52 45%,#a9a39a)}
.feature h3{font-size:27px;font-weight:700;line-height:36px;color:var(--ink);letter-spacing:.5px}
.feature p{font-size:13px;line-height:22px;color:var(--grey);margin-top:16px;width:400px}
.btn-line{display:inline-block;margin-top:26px;border:1px solid var(--grey);padding:18px 64px;font-size:12px;font-weight:600;color:var(--ink)}

/* testimonials */
.testi-bg{left:0;top:2873px;width:1200px;height:497px;background:var(--light)}
.card{top:3033px;width:417px;height:277px;background:var(--white);box-shadow:0 2px 10px rgba(0,0,0,.08);text-align:center;padding:55px 40px 0}
.card p{font-size:12px;line-height:20px;color:var(--grey)}
.avatar{width:50px;height:50px;border-radius:50%;background:linear-gradient(135deg,#d9a441,#ffc214);margin:22px auto 8px}
.card h4{font-size:14px;font-weight:600}
.card small{font-size:11px;color:var(--muted)}
.side-arrow{top:3100px;width:44px;height:48px;background:var(--gold);display:flex;align-items:center;justify-content:center}

/* social strip */
.strip{left:0;top:3373px;width:1200px;height:244px;display:flex}
.strip div{flex:1}
.link-tile{left:1040px;top:3455px;width:78px;height:78px;background:var(--gold);display:flex;align-items:center;justify-content:center}

/* footer */
.footer{left:0;top:3617px;width:1200px;height:383px;background:var(--ink);color:var(--white)}
.footer h4{font-size:15px;font-weight:600;letter-spacing:.5px;padding-bottom:10px;border-bottom:2px solid var(--gold);display:inline-block}
.footer .col{top:60px}
.footer li{list-style:none;font-size:12px;color:var(--silver);line-height:32px;display:flex;align-items:center;gap:8px;white-space:nowrap}
.contact{width:215px}
.contact li.web{font-size:11px}
.socials{display:flex;gap:8px;margin-top:20px}
.socials span{width:26px;height:26px;background:var(--white)}
.badge{width:80px;height:44px;background:#4aa0e0;border-radius:4px;margin-top:14px}
.news p{font-size:13px;color:var(--silver);margin:22px 0 14px}
.news .field{display:flex}
.news .field span{width:320px;height:38px;background:var(--white);font-size:12px;color:var(--muted);padding:11px 12px}
.news .field b{width:52px;height:38px;background:var(--gold);display:flex;align-items:center;justify-content:center}
.cards{display:flex;gap:8px;margin-top:24px;margin-left:70px}
.cards span{width:54px;height:30px;border-radius:4px;background:var(--white)}
.cards span.p{width:80px;background:none;font-family:"Montserrat",sans-serif;font-size:14px;color:var(--white);font-weight:600;padding-top:6px}
.bottom{left:170px;top:305px;width:860px;border-top:1px solid #333;padding-top:20px;font-size:12px;color:var(--silver)}
.to-top{right:170px;top:318px;width:36px;height:36px;background:var(--gold);display:flex;align-items:center;justify-content:center}
</style>
</head>
<body>

<!-- header -->
<div class="abs topbar"></div>
<div class="abs burger"><i></i><i></i><i></i></div>
<div class="abs brand"><span class="brand-dot"></span><span class="brand-name">Tidal Bloomz</span></div>
<div class="abs head-tools">
  <span class="phone">
    <svg width="14" height="14" viewBox="0 0 24 24" fill="#ffc214"><path d="M6.6 10.8a15.1 15.1 0 006.6 6.6l2.2-2.2c.3-.3.7-.4 1-.2 1.1.4 2.3.6 3.6.6.6 0 1 .4 1 1V20c0 .6-.4 1-1 1A17 17 0 013 4c0-.6.4-1 1-1h3.5c.6 0 1 .4 1 1 0 1.3.2 2.5.6 3.6.1.3 0 .7-.2 1z"/></svg>
    021 07351942
  </span>
  <svg width="16" height="16" viewBox="0 0 24 24" fill="none" stroke="#ffc214" stroke-width="2.5"><circle cx="10" cy="10" r="7"/><path d="M15 15l6 6"/></svg>
  <svg width="16" height="16" viewBox="0 0 24 24" fill="#fff"><circle cx="12" cy="8" r="5"/><path d="M3 22c0-5 4-8 9-8s9 3 9 8z"/></svg>
  <svg width="18" height="16" viewBox="0 0 24 22" fill="#fff"><path d="M1 2h4l3 12h12l3-9H7"/><circle cx="9" cy="19" r="2"/><circle cx="19" cy="19" r="2"/></svg>
</div>

<!-- hero -->
<div class="abs hero" role="img" aria-label="Close-up photo of a gold sovereign coin ring on grey stone"></div>
<h1 class="abs hero-title">THE BEST <em>SOVEREIGN</em><br>COLLECTIONS</h1>
<div class="abs hero-arrow" style="left:22px"><svg width="12" height="12" viewBox="0 0 12 12"><path d="M8 1L3 6l5 5" stroke="#1b1b1b" stroke-width="2" fill="none"/></svg></div>
<div class="abs hero-arrow" style="right:22px"><svg width="12" height="12" viewBox="0 0 12 12"><path d="M4 1l5 5-5 5" stroke="#1b1b1b" stroke-width="2" fill="none"/></svg></div>
<div class="abs thumb-arrow" style="left:180px"><svg width="8" height="10" viewBox="0 0 8 10"><path d="M6 1L2 5l4 4" stroke="#fff" stroke-width="2" fill="none"/></svg></div>
<div class="abs thumbs">
  <div class="thumb" role="img" aria-label="Gold sovereign ring"></div>
  <div class="thumb" role="img" aria-label="Sovereign coins"></div>
  <div class="thumb" role="img" aria-label="Signet ring"></div>
  <div class="thumb" role="img" aria-label="Coin pendant"></div>
  <div class="thumb" role="img" aria-label="Sovereign bracelet"></div>
</div>
<div class="abs thumb-arrow" style="left:998px"><svg width="8" height="10" viewBox="0 0 8 10"><path d="M2 1l4 4-4 4" stroke="#fff" stroke-width="2" fill="none"/></svg></div>

<!-- categories & sale -->
<nav class="abs menu">
  <a>NEW ARRIVALS</a>
  <a>BEST SELLERS</a>
  <a>FEATURED PRODUCTS</a>
  <a>SALE! <span class="new">New</span></a>
</nav>
<div class="abs sale">
  <div class="abs sale-copy">
    <h2>SALE</h2>
    <p>UP TO 40% OFF</p>
    <p class="sub">SOVEREIGN RINGS</p>
    <span class="btn btn-gold" style="margin-top:26px;margin-left:30px">SHOP NOW</span>
  </div>
  <div class="abs sale-photo" role="img" aria-label="Silver signet ring with crest"></div>
</div>

<!-- products -->
<h2 class="abs section-title" style="top:1090px">OUR PRODUCTS</h2>
<div class="abs tabs">
  <span class="on">ALL</span><span>RINGS</span><span>PENDANTS</span><span>BRACELET</span><span>COIN</span><span>CULTURAL &amp; CUSTOM PIECES</span>
</div>

<div class="abs product" style="left:173px;top:1260px"><div class="shot" role="img" aria-label="Silver medallion coin pendant"></div><h4>STERLING SILVER MEDALLION COIN</h4><span class="price">$199</span></div>
<div class="abs product" style="left:390px;top:1260px"><div class="shot" role="img" aria-label="Gold full sovereign coin"></div><h4>GOLD FULL SOVEREIGN COIN</h4><span class="price">$2499</span></div>
<div class="abs product" style="left:610px;top:1260px"><div class="shot" role="img" aria-label="Gold ring mount"></div><h4>SOVEREIGN GOLD RING MOUNT</h4><span class="price">$899</span></div>
<div class="abs product" style="left:830px;top:1260px"><div class="shot" role="img" aria-label="Gold pendant mount"></div><h4>GOLD PENDANT MOUNT</h4><span class="price">$349</span></div>

<div class="abs product" style="left:173px;top:1625px"><div class="shot" role="img" aria-label="Sovereign coin bracelet"></div><h4>SOVEREIGN BRACELET</h4><span class="price"><s>$3800</s>$2950</span></div>
<div class="abs product" style="left:390px;top:1625px"><div class="shot" role="img" aria-label="Pair of sovereign rings"></div><h4>SOVEREIGN RINGS</h4><span class="price">$1299</span></div>
<div class="abs product" style="left:610px;top:1625px"><div class="shot" role="img" aria-label="Silver medallion ring"></div><h4>SAMOA MEDALLION RING</h4><span class="price">$649</span></div>
<div class="abs product" style="left:830px;top:1625px"><div class="shot" role="img" aria-label="Silver medallion coin"></div><h4>SAMOA MEDALLION COIN</h4><span class="price">$149</span></div>

<span class="abs btn btn-gold view-more">VIEW MORE</span>

<!-- feature: collection -->
<div class="abs photo" style="left:173px;top:2123px;width:417px;height:310px" role="img" aria-label="Sovereign coins set with diamonds on black cloth"></div>
<div class="abs feature" style="left:610px;top:2160px">
  <h3>SOVEREIGN COIN WITH<br>DIAMONDS SET COLLECTION</h3>
  <p>Each coin is hand set with bright diamonds in a secure bezel, finished by our jewellers and made to last for many generations.</p>
  <span class="btn btn-line">READ MORE</span>
</div>

<!-- feature: inspiration -->
<div class="abs feature" style="left:173px;top:2555px">
  <h3>THE INSPIRATION</h3>
  <p>Everyone deserves a special piece of treasure. At Tidal Bloomz we provide you with unique, high-quality and affordable Sovereign rings &amp; pendants.</p>
  <span class="btn btn-line">READ MORE</span>
</div>
<div class="abs photo" style="left:610px;top:2483px;width:417px;height:310px;background:linear-gradient(135deg,#5c5a57,#a8a49d 50%,#6e6b67)" role="img" aria-label="Rows of silver coin pendants on grey stone"></div>

<!-- testimonials -->
<div class="abs testi-bg"></div>
<h2 class="abs section-title" style="top:2935px">TESTIMONIALS</h2>
<div class="abs" style="left:596px;top:2985px;width:8px;height:8px;background:var(--silver)"></div>
<div class="abs side-arrow" style="left:22px"><svg width="10" height="12" viewBox="0 0 10 12"><path d="M7 1L2 6l5 5" stroke="#1b1b1b" stroke-width="2" fill="none"/></svg></div>
<div class="abs card" style="left:173px">
  <p>My ring arrived fast and looks even better in person. The finish is superb and the price was very fair. Thank you so much.</p>
  <div class="avatar"></div>
  <h4>Sara Doe</h4>
  <small>Business Executive</small>
</div>
<div class="abs card" style="left:610px">
  <p>Beautiful pendant for my father, made with real care. Great service from start to finish and a piece our family will treasure.</p>
  <div class="avatar"></div>
  <h4>Chris Doe</h4>
  <small>Admin Executive</small>
</div>
<div class="abs side-arrow" style="left:1134px"><svg width="10" height="12" viewBox="0 0 10 12"><path d="M3 1l5 5-5 5" stroke="#1b1b1b" stroke-width="2" fill="none"/></svg></div>

<!-- social strip -->
<div class="abs strip">
  <div role="img" aria-label="Customers wearing jewellery" style="background:linear-gradient(135deg,#3c2a23,#8a2d2d)"></div>
  <div role="img" aria-label="Customer in team jersey" style="background:linear-gradient(135deg,#5a1e22,#c23a3a)"></div>
  <div role="img" aria-label="Customer in red shirt" style="background:linear-gradient(135deg,#b4262b,#e5e5e5)"></div>
  <div role="img" aria-label="Engraved sovereign ring" style="background:linear-gradient(135deg,#6c6863,#b9b5ae)"></div>
  <div role="img" aria-label="Coin pendant close-up" style="background:linear-gradient(135deg,#4d4a45,#b1975f)"></div>
  <div role="img" aria-label="Ring close-up" style="background:linear-gradient(135deg,#2a2a2a,#5b5b5b)"></div>
</div>
<div class="abs link-tile"><svg width="30" height="30" viewBox="0 0 24 24" fill="none" stroke="#fff" stroke-width="2"><rect x="4" y="4" width="16" height="16"/><path d="M10 14l6-6M11 8h5v5"/></svg></div>

<!-- footer -->
<footer class="abs footer">
  <div class="abs col contact" style="left:170px">
    <h4>CONTACT US</h4>
    <ul style="margin-top:14px">
      <li>Reko Tumanu</li>
      <li><svg width="12" height="12" viewBox="0 0 24 24" fill="#ffc214"><path d="M6.6 10.8a15.1 15.1 0 006.6 6.6l2.2-2.2c.3-.3.7-.4 1-.2 1.1.4 2.3.6 3.6.6.6 0 1 .4 1 1V20c0 .6-.4 1-1 1A17 17 0 013 4c0-.6.4-1 1-1h3.5c.6 0 1 .4 1 1 0 1.3.2 2.5.6 3.6.1.3 0 .7-.2 1z"/></svg>021 07351942</li>
      <li class="web"><svg width="12" height="12" viewBox="0 0 24 24" fill="none" stroke="#ffc214" stroke-width="2.5"><circle cx="12" cy="12" r="9"/><path d="M3 12h18M12 3c3 3 3 15 0 18M12 3c-3 3-3 15 0 18"/></svg>www.tidalbloomz-example.co.nz</li>
    </ul>
    <div class="socials"><span aria-label="Friendlio"></span><span aria-label="Picorama"></span><span aria-label="Swapzo"></span><span aria-label="Email"></span></div>
  </div>
  <div class="abs col" style="left:400px">
    <h4>INFORMATION</h4>
    <div style="display:flex;gap:24px;margin-top:14px">
      <ul><li>About Us</li><li>Sovereign Rings</li><li>Pendants</li><li>Bracelet</li></ul>
      <ul><li>Coin</li><li>Cultural &amp; Custom Pieces</li><li>Testimonials</li><li>FAQ</li></ul>
    </div>
    <div class="badge"></div>
  </div>
  <div class="abs col news" style="left:683px">
    <h4>NEWSLETTER</h4>
    <p>SIGN UP FOR OUR NEWSLETTER FOR LATEST UPDATES</p>
    <div class="field"><span>Email</span><b><svg width="14" height="12" viewBox="0 0 14 12"><path d="M1 6h11M8 2l4 4-4 4" stroke="#1b1b1b" stroke-width="2" fill="none"/></svg></b></div>
    <div class="cards"><span class="p">Payments</span><span></span><span></span><span></span></div>
  </div>
  <div class="abs bottom">© Copyright Information here</div>
  <div class="abs to-top"><svg width="12" height="8" viewBox="0 0 12 8"><path d="M1 7l5-5 5 5" stroke="#1b1b1b" stroke-width="2" fill="none"/></svg></div>
</footer>

</body>
</html>
```